Halvorn spray foam and Environmental

I have business cards but need new ones. The ones I have are very bland. Here is. Y company website http://www.halvornsprayfoam.ca

Also I can send you copies of the current cards
I would also need my current logo on the new design as well.. Also spray foam and Environmental

Industry/Entity Type

Business

Logo Text

Halvorn.

```html
<!DOCTYPE html>
<html lang="en">
<head>
<meta charset="utf-8">
<title>Halvorn Business Card</title>
<link rel="stylesheet" href="https://fonts.googleapis.com/css2?family=Source+Sans+3:wght@400;600;700&display=swap">
<style>
  :root {
    --backdrop: #9fcfa8;
    --card: #ffffff;
    --panel: #e2d9e8;
    --brand: #4e1e6e;
    --ink: #1f1f1f;
    --mark: #8a8a8f;
  }
  * { box-sizing: border-box; margin: 0; padding: 0; }
  html, body { width: 1200px; height: 1000px; overflow: hidden; }
  body {
    background: var(--backdrop);
    font-family: "Source Sans 3", Arial, sans-serif;
    color: var(--ink);
    display: flex;
    flex-direction: column;
    align-items: center;
    justify-content: center;
    gap: 70px;
  }
  .card {
    width: 700px;
    height: 400px;
    background: var(--card);
    box-shadow: 0 6px 18px rgba(0,0,0,0.18);
    position: relative;
    overflow: hidden;
  }
  .brand { display: flex; align-items: center; gap: 14px; }
  .brand-square { width: 46px; height: 46px; background: var(--mark); }
  .brand-name {
    color: var(--brand);
    font-weight: 700;
    font-size: 38px;
    letter-spacing: 0.5px;
    text-transform: uppercase;
  }
  /* Front */
  .card-front { display: flex; }
  .front-identity {
    width: 40%;
    display: flex;
    align-items: center;
    justify-content: center;
  }
  .front-identity .brand { flex-direction: column; gap: 10px; }
  .front-identity .brand-square { width: 70px; height: 70px; }
  .front-contacts {
    width: 60%;
    background: var(--panel);
    padding: 64px 40px 0 44px;
  }
  .division + .division { margin-top: 34px; }
  .division-title {
    color: var(--brand);
    font-weight: 700;
    font-size: 24px;
    text-transform: uppercase;
    margin-bottom: 6px;
  }
  .contact-line { font-size: 18px; line-height: 1.3; }
  .contact-line.phone { font-weight: 700; }
  .contact-label { font-weight: 700; }
  /* Back */
  .card-back {
    padding: 40px 50px 0;
    text-align: center;
  }
  .card-back .brand { justify-content: center; }
  .back-rule {
    border: 0;
    border-top: 2px solid var(--brand);
    margin: 18px 0 22px;
  }
  .service-title {
    color: var(--brand);
    font-weight: 700;
    font-size: 24px;
    text-transform: uppercase;
  }
  .service-list {
    font-size: 17px;
    text-transform: uppercase;
    line-height: 1.3;
    margin-bottom: 18px;
  }
</style>
</head>
<body>
  <section class="card card-front">
    <div class="front-identity">
      <div class="brand">
        <span class="brand-square"></span>
        <span class="brand-name">Halvorn</span>
      </div>
    </div>
    <div class="front-contacts">
      <div class="division">
        <h2 class="division-title">Spray Foam</h2>
        <p class="contact-line phone">(555) 301 - 4726</p>
        <p class="contact-line"><span class="contact-label">E</span> : halvornfoam@gmail.com</p>
        <p class="contact-line"><span class="contact-label">W</span> : www.halvornsprayfoam.ca</p>
      </div>
      <div class="division">
        <h2 class="division-title">Environmental</h2>
        <p class="contact-line phone">(555) 807 - 2193</p>
        <p class="contact-line"><span class="contact-label">E</span> : halvornenviro1@gmail.com</p>
        <p class="contact-line"><span class="contact-label">W</span> : www.halvornenvironmental.ca</p>
      </div>
    </div>
  </section>

  <section class="card card-back">
    <div class="brand">
      <span class="brand-square"></span>
      <span class="brand-name">Halvorn</span>
    </div>
    <hr class="back-rule">
    <h2 class="service-title">Spray Foam</h2>
    <p class="service-list">Roofing foam, slab jacking, 2 pound/ half pound,<br>sound proofing, batt insulation, attic blow in</p>
    <h2 class="service-title">Environmental</h2>
    <p class="service-list">Air monitoring, asbestos testing, asbestos removal,<br>building demolition, lead testing, mould removal</p>
  </section>
</body>
</html>
```